Non-Profit Organization Needs WordPress websiteTo Empower Women

Our client is a Non-profit organization that requires a responsively-designed WordPress website to help publish their online magazine. This website will also feature their magazine publication that they publish quarterly. The design will need to be mobile-friendly, so it looks great on all devices.

The main purpose of this site is the following, in order of importance:
1. Educate economically-challenged women to improve their lives with blog content and their online Magazine.
2. Create a Membership community for these women to help one another. THE MAIN CALL-TO-ACTION ON THE SITE IS TO MOTIVATE THE READERS TO JOIN THE FREE MEMBERSHIP COMMUNITY.
3. Recognize and Identify the contributing Organizations, and to motivate the organizations to donate money to the non-profit organization.

Here is information from the client about what they want for their website:
*********************************************************************************************
It needs to have two entrances to content: Organizations & Readers; Don't like cluttered which some magazine formats seem to be. Like edgy, yet feminine. Not sweet. Easy to navigate and find what one comes to find. Colorful.

We need: A Resources area, a Donation button prominently placed on the site, section for archived magazine articles; Place for translated issues. We will want to have a private Membership section on the site. (NOTE: These requests should be used to help create the site's navigation menu.)

Here are example websites the client likes and why. Please use them as inspiration.
http:://www.brindleloft.example color, simple design w cool buttons, uncluttered
http:://www.corvetide.example emotion with the color, ease of getting around
http:://www.quellmarrow7.example the second page has the color sections that take you to next page
http:://www.tamsinreedjournal.example not sweetly feminine, perhaps community style
http:://www.velkarun.example use of clear symbols, newer design/graphics look

Target Market(s)

The website targets 2 different audiences: Organizations that help to provide services and help to the website readers, and the Readers themselves. The Readers are mostly economically-challenged females that need inspiration and help. The Readers should be considered the Primary Target Audience, with the Organizations being secondary.

Industry/Entity Type

Non-Profit

Font styles to use
Sans Serif

Colors
f37022
fece3e

Requirements
Must have
• The final design MUST, MUST, MUST be created using Separate PSD layers for each element and graphic! PLEASE create a professional layer structure within your design, so we can code it properly.

Please do NOT use Graphics/Images where Text should be used. Examples of this are the business address, phone number, etc.

The website home page design should identify its two main audiences, the Organizations and the Readers. The main call to action is to invite the Readers to become free members of their membership community.

There MUST be an area on the home page where their online magazine can be embedded onto their site OR an image button etc that leads to the magazine. They use the http://plimbrook.example/ system to create the magazine and then embed the issues on their site. Alternatively, you could create a button, image, area, etc, where the user can click the image and then go to the magazine.

A membership login field OR a button that leads to a Members login area.

A small area on the website that either Brovanta or advertising can be used, and this MUST be BELOW the FOLD.

The site must project a sense of hope and/or empowerment for its Readers. The imagery should resonate with females who want to be inspired.
Nice to have
• There should be links or buttons to identify Spanish-speaking Readers and Portuguese-speaking Readers.
Should not have
• NO Gallery Sliders or Photo Sliders

```html
<!DOCTYPE html>
<html lang="en">
<head>
<meta charset="utf-8">
<title>RiseWell — A Magazine for Today's Inner City Woman</title>
<link rel="stylesheet" href="https://fonts.googleapis.com/css2?family=Open+Sans:ital,wght@0,400;0,600;0,700;1,400&family=Noto+Serif:ital,wght@0,400;0,700;1,400&display=swap">
<style>
:root{
  --orange:#f37022;
  --orange-dark:#d95a12;
  --yellow:#fece3e;
  --sky:#1fa5dc;
  --sky-dark:#157fb0;
  --ink:#333333;
  --muted:#6b6b6b;
  --paper:#ffffff;
  --night:#2a2a2a;
  --night-deep:#1c1c1c;
  --wood:#a86a34;
}
*{box-sizing:border-box;margin:0;padding:0}
html,body{width:1200px;height:2352px;overflow:hidden}
body{font-family:"Open Sans",Arial,sans-serif;color:var(--ink);background:var(--paper);position:relative}

/* Header */
.site-header{position:absolute;top:0;left:0;width:1200px;height:148px;background:var(--paper)}
.brand{position:absolute;left:36px;top:30px;display:flex;align-items:center;gap:12px}
.brand-mark{width:22px;height:22px;border-radius:50%;background:var(--orange)}
.brand-name{font-family:"Noto Serif",Georgia,serif;font-weight:700;font-size:54px;color:var(--orange);line-height:1}
.tagline{position:absolute;left:380px;top:22px;width:420px;text-align:center;font-size:15px;font-weight:600;letter-spacing:1px;line-height:24px;color:var(--ink);text-transform:uppercase}
.header-actions{position:absolute;right:36px;top:18px;width:330px}
.header-actions .row{display:flex;gap:10px}
.btn{display:flex;align-items:center;justify-content:center;font-weight:700;font-size:16px;text-transform:uppercase;height:42px;color:#fff}
.btn-support{background:var(--yellow);flex:1.4}
.btn-donate{background:var(--orange);flex:1}
.btn-join{margin-top:16px;height:44px;background:var(--yellow);color:var(--ink);justify-content:flex-start;padding-left:14px;gap:12px}
.btn-join .dot{width:22px;height:22px;border-radius:50%;background:var(--orange);display:flex;align-items:center;justify-content:center}

/* Nav */
.main-nav{position:absolute;top:148px;left:0;width:1200px;height:50px;background:var(--orange);display:flex;align-items:stretch;padding-left:36px}
.main-nav a{display:flex;align-items:center;padding:0 24px;color:#fff;font-size:18px;text-decoration:none;border-right:1px solid rgba(255,255,255,.35)}
.main-nav a.active{background:var(--paper);color:var(--orange)}
.nav-tools{margin-left:auto;display:flex}
.nav-tools span{width:58px;display:flex;align-items:center;justify-content:center;background:var(--orange-dark);border-left:1px solid rgba(255,255,255,.3)}

/* Hero */
.hero{position:absolute;top:198px;left:0;width:1200px;height:462px;background:linear-gradient(100deg,#bfbfbf 0%,#e8e8e8 35%,#f4e6a6 55%,#d9d9d9 75%,#a8a8a8 100%)}
.hero-art{position:absolute;inset:0}
.hero-copy{position:absolute;left:340px;top:250px;width:360px;font-family:"Noto Serif",Georgia,serif;color:var(--ink)}
.hero-copy .url{position:absolute;left:60px;top:-150px;font-size:18px;font-weight:700}
.hero-copy p{font-size:26px;line-height:34px;font-style:italic}
.hero-copy p b{color:var(--orange);font-size:34px}
.hero-side{position:absolute;right:140px;top:60px;writing-mode:vertical-rl;font-family:"Noto Serif",Georgia,serif;font-size:30px;color:var(--ink)}

/* Welcome */
.welcome{position:absolute;top:712px;left:60px;width:1080px;height:320px}
.welcome h1{font-family:"Noto Serif",Georgia,serif;font-size:28px;color:var(--orange);font-weight:700;margin-bottom:16px}
.welcome-text{position:absolute;left:0;top:0;width:560px}
.welcome-text p{font-size:13.5px;line-height:22px;color:var(--muted);margin-bottom:8px}
.read-more{display:block;text-align:right;font-size:13px;font-weight:700;color:var(--ink)}
.video{position:absolute;right:0;top:0;width:480px;height:290px;background:#111}
.video-frame{position:absolute;left:0;top:0;width:480px;height:252px;background:linear-gradient(135deg,#3c3c3c,#6a5a55 50%,#2b2b2b)}
.video-bar{position:absolute;left:0;bottom:0;width:480px;height:38px;background:#1a1a1a;display:flex;align-items:center;padding:0 14px;gap:12px}
.video-bar .track{flex:1;height:4px;background:#555}
.video-bar .track i{display:block;width:18%;height:4px;background:var(--orange)}

/* Feature buttons */
.features{position:absolute;top:1048px;left:60px;width:1080px;display:flex;gap:30px}
.feature{flex:1;height:170px;display:flex;align-items:center;justify-content:center;text-align:center;font-family:"Noto Serif",Georgia,serif;font-weight:700;font-size:32px;color:#fff;border:3px solid #ddd}
.feature.magazine{background:linear-gradient(135deg,#3a3a3a,#7a7a7a)}
.feature.donate{background:linear-gradient(135deg,#e0651d,var(--orange));color:var(--yellow)}
.feature.action{background:linear-gradient(135deg,#262626,#575757)}

/* Magazine shelf */
.magazines{position:absolute;top:1248px;left:0;width:1200px;height:310px}
.section-title{font-family:"Noto Serif",Georgia,serif;font-size:28px;font-weight:700;color:var(--orange);text-align:center}
.shelf-row{position:absolute;top:58px;left:110px;width:980px;display:flex;gap:20px}
.issue{width:180px;height:220px;box-shadow:0 4px 8px rgba(0,0,0,.3)}
.issue.current{background:var(--paper);border:3px solid var(--orange);display:flex;flex-direction:column;align-items:center;justify-content:center;text-align:center;gap:10px}
.issue.current h3{font-family:"Noto Serif",Georgia,serif;font-size:18px;color:var(--orange)}
.issue.current p{font-size:13px;color:var(--ink);line-height:18px}
.issue.current .read{background:var(--orange);color:#fff;font-weight:700;font-size:14px;padding:8px 18px}
.issue.c1{background:linear-gradient(160deg,#e9e0c8,#8b6a4a)}
.issue.c2{background:linear-gradient(160deg,#f5c77a,#c4472a)}
.issue.c3{background:linear-gradient(160deg,#f0e3b2,#5b4a38)}
.issue.c4{background:linear-gradient(160deg,#2f2f2f,#7b4d8f)}
.shelf{position:absolute;top:280px;left:90px;width:1020px;height:22px;background:linear-gradient(#c48a52,var(--wood));border-radius:2px}

/* Social feed */
.feed{position:absolute;top:1580px;left:0;width:1200px;height:460px;background:linear-gradient(180deg,#29b2e6,var(--sky) 50%,var(--sky-dark))}
.feed-head{position:absolute;top:0;left:0;width:1200px;height:36px;background:var(--sky-dark);color:#fff;text-align:center;font-size:15px;font-weight:600;line-height:36px}
.feed-handle{position:absolute;top:50px;left:480px;width:170px;height:34px;background:var(--sky-dark);color:#fff;text-align:center;font-size:13px;line-height:34px}
.feed-avatar{position:absolute;top:36px;left:660px;width:64px;height:64px;border-radius:50%;background:linear-gradient(135deg,#f4d2b8,#9a6e5a);border:3px solid #fff}
.feed-badge{position:absolute;top:112px;left:540px;width:100px;height:100px;border-radius:50%;background:#fff;display:flex;align-items:center;justify-content:center;font-weight:700;color:var(--sky-dark);font-size:15px}
.feed-text{position:absolute;top:236px;left:80px;width:1040px;text-align:center;color:#fff;font-style:italic;font-size:17px;line-height:26px}
.feed-time{position:absolute;top:326px;left:0;width:1200px;text-align:center;color:#fff;font-size:13px}
.feed-time::before,.feed-time::after{content:"";display:inline-block;width:70px;height:1px;background:rgba(255,255,255,.7);vertical-align:middle;margin:0 10px}
.stats{position:absolute;top:358px;left:450px;display:flex;gap:20px}
.stat{width:90px;text-align:center}
.stat b{display:block;background:#fff;color:var(--sky-dark);font-size:17px;padding:6px 0}
.stat span{display:block;background:var(--sky-dark);color:#fff;font-size:14px;padding:5px 0;font-weight:600}

/* Footer */
.site-footer{position:absolute;top:2040px;left:0;width:1200px;height:280px;background:var(--night);color:#cfcfcf;font-size:13px}
.footer-col{position:absolute;top:34px}
.footer-col h4{color:var(--yellow);font-family:"Noto Serif",Georgia,serif;font-weight:400;font-size:18px;margin-bottom:12px}
.footer-col li{list-style:none;line-height:22px}
.footer-col li.active{color:var(--orange)}
.col-menu{left:60px}
.col-mail{left:420px;width:330px}
.col-mail p{line-height:20px;margin-bottom:12px}
.signup{display:flex;gap:6px}
.signup span{flex:1;height:32px;background:#fff;color:#999;padding:0 10px;line-height:32px}
.signup b{width:44px;height:32px;background:var(--yellow);color:var(--ink);text-align:center;line-height:32px}
.social{display:flex;gap:10px;margin-top:16px}
.social i{width:30px;height:30px;border-radius:50%;border:2px solid #888}
.col-touch{left:880px;width:270px}
.col-touch dt{color:var(--yellow);font-style:italic;margin-top:6px}
.col-touch dd{line-height:20px}
.footer-bar{position:absolute;top:2320px;left:0;width:1200px;height:32px;background:var(--night-deep);color:#9a9a9a;font-size:12px;line-height:32px;padding:0 60px;display:flex;justify-content:space-between}
</style>
</head>
<body>

<header class="site-header">
  <div class="brand"><span class="brand-mark"></span><span class="brand-name">RiseWell</span></div>
  <p class="tagline">A magazine for the empowerment and enrichment of today's inner city woman</p>
  <div class="header-actions">
    <div class="row"><span class="btn btn-support">Get Support</span><span class="btn btn-donate">Donate</span></div>
    <div class="btn btn-join"><span class="dot"><svg width="10" height="10" viewBox="0 0 10 10"><path d="M3 1l4 4-4 4" stroke="#fff" stroke-width="2" fill="none"/></svg></span>Join Free Membership</div>
  </div>
</header>

<nav class="main-nav">
  <a class="active">Home</a><a>About Us</a><a>Online Magazine</a><a>Case Studies</a><a>Blog</a><a>Contact Us</a>
  <div class="nav-tools">
    <span><svg width="22" height="22" viewBox="0 0 22 22"><circle cx="9" cy="9" r="6" stroke="#fff" stroke-width="2.5" fill="none"/><path d="M13.5 13.5l6 6" stroke="#fff" stroke-width="3"/></svg></span>
    <span><svg width="22" height="22" viewBox="0 0 22 22"><circle cx="11" cy="7" r="4.5" fill="#fff"/><path d="M3 20c0-5 4-8 8-8s8 3 8 8z" fill="#fff"/></svg></span>
  </div>
</nav>

<section class="hero">
  <div class="hero-art" role="img" aria-label="Illustration of a woman silhouette with yellow splashes against a grey city skyline"></div>
  <div class="hero-copy">
    <span class="url">www.risewellmag.example</span>
    <p>"a magazine to <b>enrich</b><br>and <b>empower</b><br>today's urban woman"</p>
  </div>
  <div class="hero-side">RiseWell magazine</div>
</section>

<section class="welcome">
  <div class="welcome-text">
    <h1>Welcome to RiseWell</h1>
    <p>You're here because you care about people in the inner city. You don't see them as a problem or individuals to ignore. So, like those of us on the RiseWell team, you see wonderful individuals each with a story to tell. You know there is great potential in the most difficult circumstances and you want to help them reach their goals.</p>
    <p>RiseWell is a magazine designed to empower and enrich the lives of inner city women. It is distributed by a growing network of inner city ministries.</p>
    <p>RiseWell is a unique tool to help inner city women in a non-threatening, encouraging way. The articles are crafted and written with an understanding of life, real life.</p>
    <span class="read-more">Read more..</span>
  </div>
  <div class="video">
    <div class="video-frame" role="img" aria-label="Video still of a smiling woman speaking"></div>
    <div class="video-bar">
      <svg width="14" height="16" viewBox="0 0 14 16"><path d="M1 1l12 7-12 7z" fill="#fff"/></svg>
      <div class="track"><i></i></div>
      <svg width="18" height="16" viewBox="0 0 18 16"><path d="M1 5h4l5-4v14l-5-4H1z" fill="#fff"/></svg>
    </div>
  </div>
</section>

<section class="features">
  <div class="feature magazine" role="img" aria-label="Photo of magazines on a table">online Magazine</div>
  <div class="feature donate">Donate RiseWell</div>
  <div class="feature action" role="img" aria-label="Photo of raised hands">Join Free Today</div>
</section>

<section class="magazines">
  <h2 class="section-title">Online Read Magazines</h2>
  <div class="shelf-row">
    <div class="issue current"><h3>RiseWell Spring 2014</h3><p>Ft. Lauderdale, FL<br>United States</p><span class="read">Read now</span></div>
    <div class="issue c1" role="img" aria-label="Magazine cover, portrait of a woman"></div>
    <div class="issue c2" role="img" aria-label="Magazine cover, warm toned feature"></div>
    <div class="issue c3" role="img" aria-label="Magazine cover, family photo"></div>
    <div class="issue c4" role="img" aria-label="Magazine cover, purple toned feature"></div>
  </div>
  <div class="shelf"></div>
</section>

<section class="feed">
  <div class="feed-head">Lorem ipsum</div>
  <div class="feed-handle">@Lorem ipsum</div>
  <div class="feed-avatar" role="img" aria-label="Profile photo"></div>
  <div class="feed-badge">Chirpline</div>
  <p class="feed-text">Lorem ipsum dolor sit amet, consectetur adipiscing elit. Proin ultricies nunc vel consectetur vestibulum. Sed ornare semper magna et pretium. Cum sociis natoque penatibus et magnis dis parturient montes, nascetur ridiculus mus. Sed sodales dui et velit rhoncus tincidunt. Mauris vel molestie tortor.</p>
  <p class="feed-time">13 hours ago</p>
  <div class="stats">
    <div class="stat"><b>7540</b><span>Tweets</span></div>
    <div class="stat"><b>950</b><span>Following</span></div>
    <div class="stat"><b>54586</b><span>Followers</span></div>
  </div>
</section>

<footer class="site-footer">
  <div class="footer-col col-menu">
    <h4>Menu</h4>
    <ul><li class="active">Home</li><li>About Us</li><li>Online Magazine</li><li>Case Studies</li><li>Blog</li><li>Contact Us</li></ul>
  </div>
  <div class="footer-col col-mail">
    <h4>Join Our Mailing List</h4>
    <p>Lorem ipsum dolor sit amet, cons adipiscing elit. Aliquam</p>
    <div class="signup"><span>email@domain.com</span><b>GO</b></div>
    <div class="social"><i></i><i></i><i></i><i></i><i></i></div>
  </div>
  <div class="footer-col col-touch">
    <h4>Get In Touch</h4>
    <dl>
      <dt>Address</dt><dd>Lorem ipsum dolor sit amet,<br>conse adipiscing elit. Aen ligula</dd>
      <dt>Phone</dt><dd>+1 555 0142 789</dd>
      <dt>Email</dt><dd>info@risewell.example</dd>
    </dl>
  </div>
</footer>
<div class="footer-bar"><span>Copyright © 2014 RiseWell. All rights Reserved</span><span>Sitemap &nbsp;|&nbsp; Terms of Use &nbsp;|&nbsp; Privacy</span></div>

</body>
</html>
```